Law Firm St. Patrick's Day Party

Two different law firm's joining to have a St. Patrick's Day party. Invitees will include other lawyers, clients and friends. This is intended to be more of a causal event. So we are looking for an invite that is fun but not cheesy.

The invite will be a two sided "post card." One side should be the details of event and design. The opposite side should be our firm logos (see uploads) with an area on the right side for postage and mailing address. We will be providing live music, food and drinks. Also...the NVBL Basketball Tournaments will playing the same day...some sort of reference that we Will have TVs to watch the Basketball games is needed too.

Target Market(s)

Fun professional crowd

Industry/Entity Type

Law Firm

Font styles to use
Serif
Decorative
Script

Requirements
Must have
• time, date and where...food, drinks TVs (NVBL games)
• Essential Information: Friday, March 17th. The party will start at 2:00 p.m. and run until "Whenever." The location of the Party is 2846 Birch Lane, Kansas City, Missouri 64108.
Nice to have
• something festive for St. Pat's day

```html
<!DOCTYPE html>
<html lang="en">
<head>
<meta charset="utf-8">
<title>St. Patrick's Day Party Postcard</title>
<link rel="stylesheet" href="https://fonts.googleapis.com/css2?family=Lato:wght@400;700;900&family=Playball&family=Dancing+Script:wght@500&display=swap">
<style>
  :root {
    --stage: #e4e5e6;
    --paper: #f7f5ef;
    --teal: #1b7d9e;
    --teal-dark: #13617c;
    --red: #d2232a;
    --badge-text: #ffe94a;
    --gold: #8c6c3c;
    --firm-blue: #2e61a8;
    --divider: #c9c6bd;
  }
  * { box-sizing: border-box; margin: 0; padding: 0; }
  html, body { width: 1200px; height: 414px; overflow: hidden; }
  body { background: var(--stage); position: relative; font-family: "Lato", sans-serif; }

  .postcard {
    position: absolute; top: 27px; width: 540px; height: 360px;
    background: var(--paper);
    box-shadow: 0 2px 6px rgba(0,0,0,.18);
    overflow: hidden;
  }
  .postcard--back { left: 40px; }
  .postcard--front { left: 620px; }

  /* Corner ornament areas: flat teal fields shaped to the corner */
  .ornament {
    position: absolute; width: 88px; height: 78px;
    background: linear-gradient(135deg, var(--teal-dark), var(--teal));
  }
  .ornament--top-left { top: 0; left: 0; border-bottom-right-radius: 100%; }
  .ornament--bottom-left { bottom: 0; left: 0; border-top-right-radius: 100%; }
  .ornament--top-right { top: 0; right: 0; border-bottom-left-radius: 100%; }
  .ornament--bottom-right { bottom: 0; right: 0; border-top-left-radius: 100%; }

  /* Back side */
  .mail-divider {
    position: absolute; left: 270px; top: 28px; bottom: 28px; width: 1px; background: var(--divider);
  }
  .firm {
    position: absolute; left: 28px; display: flex; align-items: center; gap: 9px;
    font-weight: 700; font-size: 15px; letter-spacing: .2px; white-space: nowrap;
  }
  .firm__mark { width: 22px; height: 22px; flex: none; }
  .firm--one { top: 148px; color: var(--gold); }
  .firm--one .firm__mark { background: var(--gold); }
  .firm--two { top: 202px; color: var(--firm-blue); }
  .firm--two .firm__mark { background: var(--firm-blue); }

  /* Front side */
  .frame { position: absolute; inset: 7px; border: 4px solid var(--teal); }

  .invite-lead {
    position: absolute; top: 22px; left: 80px; width: 265px; text-align: center;
    color: var(--teal); font-size: 21px; letter-spacing: .5px;
  }
  .rule { position: absolute; height: 2px; background: var(--teal); }
  .rule--top { top: 50px; left: 28px; width: 372px; }
  .rule--top-thin { top: 55px; left: 50px; width: 300px; height: 1px; }
  .rule--bottom { top: 132px; left: 36px; width: 364px; }
  .rule--bottom-thin { top: 137px; left: 60px; width: 300px; height: 1px; }

  .event-title {
    position: absolute; top: 58px; left: 40px;
    font-family: "Playball", cursive; font-weight: 400; color: var(--teal); font-size: 44px; line-height: 1;
  }
  .event-subtitle {
    position: absolute; top: 102px; left: 240px;
    font-family: "Playball", cursive; color: var(--teal); font-size: 26px; line-height: 1;
  }
  .event-date {
    position: absolute; top: 141px; left: 60px; width: 300px; text-align: center;
    color: var(--teal); font-size: 16px; font-weight: 700;
  }
  .event-details {
    position: absolute; top: 165px; left: 22px; width: 380px; text-align: center;
    color: var(--teal); font-size: 9.5px; line-height: 1.4;
  }
  .event-details strong { font-weight: 900; }

  .basketball-art {
    position: absolute; top: 84px; left: 408px; width: 108px; height: 150px;
    background: linear-gradient(165deg, rgba(27,125,158,.10), rgba(210,35,42,.30) 60%, rgba(40,40,40,.18));
    border-radius: 6px;
  }

  .tv-badge { position: absolute; top: 200px; left: 14px; width: 96px; height: 96px; }
  .tv-badge svg { display: block; }
  .tv-badge__text {
    position: absolute; inset: 18px 12px; display: flex; align-items: center; justify-content: center;
    text-align: center; color: var(--badge-text); font-size: 8px; font-weight: 700; line-height: 1.2;
  }

  .perks {
    position: absolute; top: 240px; left: 138px; width: 268px; height: 96px;
    background: var(--teal); border-radius: 10px; color: #fff;
    font-family: "Dancing Script", cursive; font-size: 15px; line-height: 1.3;
    display: flex; align-items: center; justify-content: center; text-align: center; padding: 0 8px;
  }
</style>
</head>
<body>

<section class="postcard postcard--back" aria-label="Postcard mailing side">
  <div class="ornament ornament--top-left" role="img" aria-label="Teal floral corner ornament"></div>
  <div class="ornament ornament--bottom-left" role="img" aria-label="Teal floral corner ornament"></div>
  <div class="firm firm--one"><span class="firm__mark"></span>Harwell &amp; Stone LLC</div>
  <div class="firm firm--two"><span class="firm__mark"></span>Brandt Keller &amp; Moss, LLC</div>
  <div class="mail-divider"></div>
</section>

<section class="postcard postcard--front" aria-label="Postcard invitation side">
  <div class="frame"></div>
  <div class="ornament ornament--top-right" role="img" aria-label="Teal floral corner ornament"></div>
  <div class="ornament ornament--bottom-right" role="img" aria-label="Teal floral corner ornament"></div>

  <p class="invite-lead">YOU ARE INVITED ON</p>
  <div class="rule rule--top"></div>
  <div class="rule rule--top-thin"></div>
  <h1 class="event-title">St. Patrick's</h1>
  <p class="event-subtitle">Day party</p>
  <div class="rule rule--bottom"></div>
  <div class="rule rule--bottom-thin"></div>

  <p class="event-date">Friday, March 17th.</p>
  <p class="event-details">The party will start at <strong>2:00</strong> p.m. and run until <strong>"Whenever."</strong><br>The location of the Party is 2846 Birch Lane, Kansas City, Missouri 64108.</p>

  <div class="basketball-art" role="img" aria-label="Illustration of a basketball player leaping toward a hoop"></div>

  <div class="tv-badge">
    <svg width="96" height="96" viewBox="0 0 78 78" aria-hidden="true">
      <polygon fill="#d2232a" points="39,1 45,10 55,5 57,16 68,15 65,26 76,30 68,39 76,48 65,52 68,63 57,62 55,73 45,68 39,77 33,68 23,73 21,62 10,63 13,52 2,48 10,39 2,30 13,26 10,15 21,16 23,5 33,10"/>
    </svg>
    <p class="tv-badge__text">NVBL<br>Basketball<br>Tournaments will<br>playing the<br>same day</p>
  </div>

  <p class="perks">We will be providing live music,<br>food and drinks.<br>Also we will have TVs to watch the<br>Basketball games is needed too.</p>
</section>

</body>
</html>
```